Web Card Landing Page Template Site

Our company sells "Seen Local" packages. We submit key information about a business to major data aggregators in the USA. One of the things we submit is a domain name. So we are selling a custom domain name which will be used with a one page web card site that is has local search markup built in and is Responsive.

I am looking for a new responsive simple design from art forge optimized for search engines, desktops and mobile devices.
We sell high quantities of this package and I want to be able to change out new business information quickly in our WordPress Multi-site environment. Commented code is a must. The color layout should be neutral to fit many types of businesses.

Necessary areas on template:
Main Company Logo
Up to 5 images from customer
Business Name
Full Address
Main Phone
Toll Free
Cell Phone
Fax
email address
Website
Hours of operation
types of payments accepted (example: Paycrest | Orvo | Lumina | Cash | Check)
up to 5 categories (example:Auto Repair | Mechanic | Tire Dealers | Breaks | AC Repair)
Area for Business Description (500 or less characters will be used)
Certifications/Memberships/Specialties
year established
Map (should be a map of the business address) (not sure if this can be linked some how)
Social Icons (Chatterly+,Friendlane,Chirpit,ClipHub,WorkNest)

Our main goal is to have customers visit this business web card from a local search and to find most things there looking for at a glance and want to make a quick decision tor work with the company.
Simple enough for entry level techs or data entry employees to update each new page with new business information.
We look forward to designs. :)
Updates

Please don't hesitate to ask questions regarding this brief.

Participation money available now.

I look forward to feed back from potential designers

Thanks

Also this project is now Committed instead of Refundable.

Ok, Designers, to help clarify, this single page design you create will be used over and over and over again for different types of small businesses. it will mostly be a one size fits all type design. It will need to be used as a template for us to quickly put in new customers data and pictures and then we will point there domain name at the design. One day it could be a plumber company, another day a heating contractor and another day a a beauty salon or an insurance company.

Here is two links of something similar except this design is missing a few necessity things that is listed in my brief. View the source for ideas. I may have to extend this project, keep posted on this project. Thanks

http://brindlecreekdepot.verilisting.org/brindle/waste-management
http://tallreedpromotionsllc.verilisting.org/lark-hollow/yellow-pages

or a sample of images, and some of the necessities to be on this one pager design
http://kestavoline.com/public_html/wp-admin/images/client-images/Example.PNG

Reason: Designers requested more time. I hope the designers that didn't have the time prior take a second look. Please review the breif with a more clear understanding of scope of work.

• sample of images, and some of the necessities to be on this one pager design

```html
<!DOCTYPE html>
<html lang="en">
<head>
<meta charset="utf-8">
<title>Seen Local – Business Web Card</title>
<link rel="stylesheet" href="https://fonts.googleapis.com/css2?family=Noticia+Text:ital,wght@0,400;0,700;1,400;1,700&family=Open+Sans:wght@400;600&display=swap">
<style>
  :root {
    --orange: #d3640f;
    --blue: #0a82b3;
    --ink: #444;
    --muted: #666;
    --light: #ececec;
    --panel: #e9e9e9;
    --rule: #d6d6d6;
    --dark: #555;
    --gold: #f2c12e;
    --white: #fff;
    --serif: "Noticia Text", Georgia, serif;
    --sans: "Open Sans", Arial, sans-serif;
  }
  * { box-sizing: border-box; margin: 0; padding: 0; }
  html, body { width: 1004px; height: 1200px; overflow: hidden; }
  body { position: relative; background: var(--white); font-family: var(--sans); color: var(--ink); }
  .abs { position: absolute; }

  /* Header */
  .site-header { left: 0; top: 0; width: 1004px; height: 144px; background: var(--light); }
  .header-art { left: 212px; top: 0; width: 502px; height: 144px;
    background: linear-gradient(90deg, rgba(236,236,236,0) 0%, #e2e5ea 30%, #e6e8ec 60%, rgba(236,236,236,0) 100%); }
  .brand { left: 40px; top: 38px; font-family: var(--serif); font-weight: 700; font-size: 46px; color: var(--orange); line-height: 1; }
  .social { right: 42px; top: 18px; display: flex; gap: 6px; }
  .social span { display: flex; align-items: center; gap: 3px; font-family: var(--serif); font-size: 10px; color: var(--dark); }
  .social span::before { content: ""; width: 8px; height: 8px; background: #9a9a9a; }
  .contact-top { right: 42px; top: 58px; text-align: right; font-family: var(--serif); font-style: italic; font-size: 17px; line-height: 25px; color: var(--ink); }
  .contact-top b { font-weight: 400; color: var(--orange); }
  .contact-top .email { font-size: 14px; }

  /* Navigation */
  .main-nav { left: 40px; top: 144px; width: 923px; height: 50px; background: var(--white); display: flex; }
  .main-nav a { display: flex; align-items: center; padding: 0 24px; font-family: var(--serif); font-size: 17px; color: var(--ink); text-decoration: none; border-right: 1px solid var(--rule); }
  .main-nav a.active { background: var(--blue); color: var(--white); font-weight: 700; }
  .search { flex: 1; display: flex; align-items: center; padding-left: 17px; font-size: 12px; font-style: italic; color: #999; }
  .search-btn { width: 46px; background: var(--blue); display: flex; align-items: center; justify-content: center; }

  /* Hero */
  .hero-band { left: 0; top: 248px; width: 1004px; height: 243px; background: var(--blue); }
  .hero-shadow { left: 80px; top: 530px; width: 844px; height: 20px; border-radius: 50%; box-shadow: 0 12px 18px rgba(0,0,0,.25); }
  .lead-form { left: 40px; top: 194px; width: 262px; height: 349px; background: var(--orange); color: var(--white); }
  .lead-form h2 { font-family: var(--serif); font-weight: 400; font-size: 14px; line-height: 1.2; padding: 16px 19px 12px; border-bottom: 1px solid rgba(255,255,255,.35); }
  .lead-form h2 strong { display: block; font-size: 21px; font-weight: 400; }
  .field { position: absolute; left: 19px; width: 225px; height: 31px; background: var(--white); font-size: 11px; font-style: italic; color: #777; padding: 8px 10px; }
  .submit { position: absolute; left: 122px; top: 294px; width: 122px; height: 37px; background: #111; font-family: var(--serif); font-weight: 700; font-size: 16px; display: flex; align-items: center; justify-content: center; }
  .hero-photo { left: 302px; top: 194px; width: 661px; height: 349px; background: linear-gradient(135deg, #efe9e4 0%, #d9d3cd 45%, #8d8f95 75%, #c9c9c9 100%); }
  .hero-caption { left: 302px; top: 471px; width: 661px; height: 72px; background: rgba(15,15,15,.85); padding: 9px 29px; }
  .hero-caption h1 { font-family: var(--serif); font-weight: 400; font-size: 27px; color: var(--gold); line-height: 1.2; }
  .hero-caption p { font-family: var(--serif); font-size: 14px; color: #ddd; margin-top: 3px; }

  /* Feature cards */
  .feature { width: 287px; height: 181px; top: 580px; background: var(--white); border: 1px solid #ddd; box-shadow: 0 1px 4px rgba(0,0,0,.25); padding: 5px; }
  .feature .thumb { height: 139px; background: linear-gradient(135deg, #b9b9b9, #6d6d6d); }
  .feature .label { height: 32px; display: flex; align-items: center; justify-content: center; font-family: var(--serif); font-style: italic; font-size: 16px; color: var(--white); background: #666; }
  .feature .label.blue { background: var(--blue); }
  .feature .thumb.color { background: linear-gradient(135deg, #8f9aa8, #52596a 60%, #b0907a); }

  /* Categories */
  .categories { left: 40px; top: 788px; width: 226px; }
  .categories h3 { height: 37px; background: var(--orange); color: var(--white); font-family: var(--serif); font-weight: 400; font-size: 19px; padding: 5px 12px; }
  .categories li { list-style: none; height: 32px; border-bottom: 2px solid #fff; background: var(--panel); font-size: 12.5px; color: var(--muted); display: flex; align-items: center; padding-left: 13px; }
  .categories li::before { content: "»"; margin-right: 9px; }
  .categories li.active { background: var(--blue); color: var(--white); font-weight: 600; }

  /* Welcome text */
  .welcome { left: 292px; top: 785px; width: 671px; }
  .welcome h2 { font-family: var(--serif); font-weight: 400; font-size: 21px; color: var(--orange); padding-bottom: 8px; border-bottom: 1px solid var(--rule); }
  .welcome p { font-size: 12.3px; line-height: 22.3px; color: var(--muted); margin-top: 7px; }
  .welcome .link-icon { position: absolute; right: 0; top: 10px; }

  /* Footer */
  .site-footer { left: 0; top: 1015px; width: 1004px; height: 140px; background: var(--panel); }
  .map { left: 41px; top: 1034px; width: 327px; height: 79px; background: linear-gradient(90deg, #d9dcc8, #ece9dc 50%, #e4e2d5); border: 1px solid #ccc; }
  .address { left: 41px; top: 1122px; font-size: 12.3px; color: var(--ink); }
  .contact-list { left: 386px; top: 1034px; width: 306px; }
  .contact-list li { list-style: none; height: 28px; display: flex; align-items: center; justify-content: space-between; border-bottom: 1px solid #d3d3d3; font-size: 12.3px; }
  .contact-list li:last-child { border: 0; }
  .contact-list .key { display: flex; align-items: center; gap: 8px; color: var(--blue); }
  .payments { left: 810px; top: 1037px; width: 152px; display: grid; grid-template-columns: repeat(3, 44px); gap: 15px 10px; }
  .payments span { height: 30px; background: var(--white); border: 1px solid #c9c9c9; border-radius: 4px; display: flex; align-items: center; justify-content: center; font-family: var(--sans); font-weight: 600; font-size: 8.5px; color: var(--dark); }
  .bottom-bar { left: 0; top: 1155px; width: 1004px; height: 45px; background: var(--dark); }
  .copyright { left: 40px; top: 1168px; font-size: 12px; color: #ddd; }
  .newsletter { left: 638px; top: 1166px; display: flex; align-items: center; gap: 14px; }
  .newsletter b { font-size: 14px; font-weight: 600; color: var(--white); }
  .newsletter .input { width: 241px; height: 25px; background: var(--white); display: flex; align-items: center; padding-left: 6px; gap: 6px; font-size: 10px; font-style: italic; color: #aaa; position: relative; }
  .newsletter .go { position: absolute; right: 3px; top: 3px; width: 19px; height: 19px; background: var(--blue); }
</style>
</head>
<body>

<header class="site-header abs"></header>
<div class="header-art abs" role="img" aria-label="Faint stack of payment cards"></div>
<div class="brand abs">Seen Local</div>
<div class="social abs">
  <span>Friendlane</span><span>Chirpit</span><span>Chatterly+</span><span>WorkNest</span><span>ClipHub</span>
</div>
<div class="contact-top abs">
  <div><b>Toll Free:</b> 123 456 7890</div>
  <div><b>Fax:</b> 0123 456 78900</div>
  <div class="email"><b>Email:</b> info@seenlocal.com</div>
</div>

<nav class="main-nav abs">
  <a class="active">Home</a><a>About Us</a><a>Services</a><a>Categories</a><a>News</a><a>Contact Us</a>
  <div class="search">Serach...</div>
  <div class="search-btn">
    <svg width="24" height="24" viewBox="0 0 24 24" fill="none" stroke="#fff" stroke-width="2.6"><circle cx="14" cy="10" r="6.5"/><path d="M9.3 14.7 3 21" stroke-linecap="round"/></svg>
  </div>
</nav>

<div class="hero-band abs"></div>
<div class="hero-shadow abs"></div>
<form class="lead-form abs">
  <h2>Fill uot the form below to <strong>Seen Local</strong></h2>
  <div class="field" style="top:84px">First name:</div>
  <div class="field" style="top:124px">Last name:</div>
  <div class="field" style="top:165px">Email:</div>
  <div class="field" style="top:205px">Phone:</div>
  <div class="field" style="top:246px">Zip code:</div>
  <div class="submit">Submit info</div>
</form>
<div class="hero-photo abs" role="img" aria-label="Businessman handing a card to a smiling client in an office"></div>
<div class="hero-caption abs">
  <h1>Lorem ipsum dolor sit amet</h1>
  <p>Etiam iaculis turpis eu magna placerat auctor.tiam iaculis turpis eu</p>
</div>

<div class="feature abs" style="left:45px">
  <div class="thumb color" role="img" aria-label="Business team meeting with a client"></div>
  <div class="label blue">Personal services</div>
</div>
<div class="feature abs" style="left:358px">
  <div class="thumb" role="img" aria-label="Agent handing a card to a client"></div>
  <div class="label">Instant coverage</div>
</div>
<div class="feature abs" style="left:672px">
  <div class="thumb" role="img" aria-label="Hand dropping a coin into a piggy bank"></div>
  <div class="label">Save money</div>
</div>

<aside class="categories abs">
  <h3>Categories</h3>
  <ul>
    <li class="active">Auto Repair</li><li>Mechanic</li><li>Tire Dealers</li><li>Breaks</li><li>AC Repair</li>
  </ul>
</aside>

<section class="welcome abs">
  <h2>Welcome to Seen Local</h2>
  <svg class="link-icon" width="24" height="24" viewBox="0 0 24 24" fill="none" stroke="#aaa" stroke-width="3" stroke-linecap="round"><path d="M10 14 14 10"/><path d="M8 12l-3 3a3 3 0 0 0 4 4l3-3"/><path d="M16 12l3-3a3 3 0 0 0-4-4l-3 3"/></svg>
  <p>Lorem ipsum dolor sit amet, consectetur adipiscing elit. Vivamus rhoncus, sem at sollicitudin semper, lectus sem egestas est, non pellentesque risus velit vehicula velit. Mauris dictum elementum risus, at egestas nisi euismod a. In hac habitasse platea dictumst. Duis imperdiet commodo volutpat. Duis vel libero fringilla, aliquam libero sed, facilisis velit . Duis malesuada ipsum vitae mi bibendum, id ultrices sem sodales.</p>
  <p>Duis imperdiet commodo volutpat. Duis vel libero fringilla, aliquam libero sed, facilisis velit. Duis malesuada ipsum vitae mi bibendum, id ultrices sem sodales. Fusce in nulla ornare, convallis est sit amet, blandit sapien. Nulla rutrum tortor eu condimentum accumsan. Pellentesque sed est vitae quam iaculis laoreet in a tortor.</p>
</section>

<footer class="site-footer abs"></footer>
<div class="map abs" role="img" aria-label="Map of the business location"></div>
<div class="address abs">S43 Lorem Ipsum, amet Consctetur, Loremipsum - B29 6US</div>
<ul class="contact-list abs">
  <li><span class="key"><svg width="16" height="12" viewBox="0 0 16 12"><rect width="16" height="12" fill="#0a82b3"/><path d="M0 0l8 6 8-6" stroke="#fff" fill="none" stroke-width="1.4"/></svg>Mail</span>info@seenlocal.com</li>
  <li><span class="key"><svg width="16" height="16" viewBox="0 0 16 16"><path d="M3 1l3 3-2 2c1 2 4 5 6 6l2-2 3 3-2 2C7 15 1 9 1 3z" fill="#0a82b3"/></svg>Telephone</span>123 456 7890</li>
  <li><span class="key"><svg width="16" height="16" viewBox="0 0 16 16"><rect x="1" y="6" width="14" height="9" fill="#0a82b3"/><rect x="4" y="1" width="8" height="6" fill="#0a82b3"/><rect x="4" y="10" width="8" height="2" fill="#fff"/></svg>Fax</span>0123 456 7890</li>
</ul>
<div class="payments abs">
  <span>Paycrest</span><span>Orvo</span><span>Meridian</span>
  <span>Cadence</span><span>Nimbus</span><span>Paydrift</span>
</div>

<div class="bottom-bar abs"></div>
<div class="copyright abs">Copyright © 2013 Seen Local. All rights reserved.</div>
<div class="newsletter abs">
  <b>Newsletter</b>
  <div class="input">
    <svg width="13" height="10" viewBox="0 0 16 12"><rect width="16" height="12" fill="#bbb"/><path d="M0 0l8 6 8-6" stroke="#fff" fill="none" stroke-width="1.4"/></svg>
    your email
    <span class="go"><svg width="19" height="19" viewBox="0 0 19 19"><path d="M5 4l10 5.5L5 15z" fill="#fff"/></svg></span>
  </div>
</div>

</body>
</html>
```